Dravetti Business Cards

We need a business card design for Dravetti Mining.

This is a B2B company that buys and sells large machinery tires within the coal mining industry. The design should the strong, crisp and masculine. I have uploaded the company logo and rough mock-up of what the back of the card should look like. the front of the card should have the same look/feel as the back. I need editable templates for both the front and the back of the card.

Color scheme should be grey/green/black

Contact information to include on the card:
Name: Owen Pellsworth
Title: Managing Director
Phone: 972-555-0143
Address: 3157 Brantley #5 Dallas, TX 75209
Email: Owen@Dravetti-example.com

I am also opening a contest for letterhead design. If you submit a business card design, please also submit a letterhead design with the same look/feel. The winner of the business card design will also will the letter head and be paid for both.

Target Market(s)

Procurement men/women in the coal mining industry

Industry/Entity Type

Coal Mining

```html
<!DOCTYPE html>
<html lang="en">
<head>
<meta charset="utf-8">
<title>Dravetti Mining – Business Cards</title>
<link rel="stylesheet" href="https://fonts.googleapis.com/css2?family=Montserrat:wght@400;600;700&display=swap">
<style>
  :root {
    --backdrop: #4a4b4c;
    --card-light: #f4f4f3;
    --card-dark: #222324;
    --ink-dark: #3f4244;
    --ink-mid: #55585a;
    --ink-light: #e9eaea;
    --accent-green: #3f9a1c;
  }
  * { margin: 0; padding: 0; box-sizing: border-box; }
  html, body {
    width: 1200px; height: 1000px; overflow: hidden;
    background: var(--backdrop);
    font-family: "Montserrat", sans-serif;
  }
  .canvas { position: relative; width: 1200px; height: 1000px; }

  .card {
    position: absolute;
    width: 532px; height: 302px;
    overflow: hidden;
    box-shadow: 0 3px 8px rgba(0,0,0,0.35);
  }
  .card--front { left: 190px; top: 172px; background: var(--card-light); }
  .card--back  { left: 486px; top: 559px; background: var(--card-dark); }

  .brand { position: absolute; display: flex; align-items: center; }
  .brand__square { background: var(--accent-green); flex: none; }
  .brand__name { font-weight: 700; letter-spacing: 0.5px; white-space: nowrap; line-height: 1; }

  .card--front .brand { left: 32px; top: 130px; gap: 11px; }
  .card--front .brand__square { width: 40px; height: 40px; }
  .card--front .brand__name { font-size: 21px; color: var(--ink-dark); }

  .card--back .brand { left: 54px; top: 118px; gap: 20px; }
  .card--back .brand__square { width: 62px; height: 62px; }
  .card--back .brand__name { font-size: 33px; color: var(--ink-light); }

  .info-block {
    position: absolute; left: 316px;
    border-left: 3px solid var(--accent-green);
    padding-left: 22px;
    color: var(--ink-mid);
  }
  .info-block--person { top: 38px; height: 62px; padding-top: 12px; }
  .info-block--contact { top: 201px; height: 64px; padding-top: 4px; font-style: normal; }

  .person__name { font-size: 14px; font-weight: 700; color: var(--ink-dark); letter-spacing: 0.3px; text-transform: uppercase; white-space: nowrap; }
  .person__title { font-size: 12px; margin-top: 2px; }

  .contact__line { font-size: 10.5px; line-height: 15px; white-space: nowrap; }
  .contact__label { color: var(--accent-green); font-weight: 700; }
</style>
</head>
<body>
<main class="canvas">
  <section class="card card--front" aria-label="Business card front">
    <div class="brand">
      <span class="brand__square"></span>
      <span class="brand__name">DRAVETTI MINING</span>
    </div>
    <div class="info-block info-block--person">
      <p class="person__name">Owen Pellsworth</p>
      <p class="person__title">Managing Director</p>
    </div>
    <address class="info-block info-block--contact">
      <p class="contact__line">3157 Brantley #5</p>
      <p class="contact__line">Dallas, TX 75209</p>
      <p class="contact__line"><span class="contact__label">T:</span> 972-555-0143</p>
      <p class="contact__line"><span class="contact__label">E:</span> Owen@Dravetti-example.com</p>
    </address>
  </section>

  <section class="card card--back" aria-label="Business card back">
    <div class="brand">
      <span class="brand__square"></span>
      <span class="brand__name">DRAVETTI MINING</span>
    </div>
  </section>
</main>
</body>
</html>
```